4-Seiten Flyer-Design - alter Flyer als Anregung
Zielgruppe
Wir sind ein lokales Augenoptikfachgeschäft
Aufgabenstellung
Als Anlage ist unser alter Flyer - Wir möchten, dass Design einfach frischer wird. Wichtig wäre es, möglichst wenig blau oder rot-Bereiche zu haben. Dieses sind eher die Farben der Mitbewerber.
Als Anlage ist unser Flyer vom letzten Mal. Die Texte bzw. Preise müssen nach Vorgabe der word bzw. Exceldatei geändert werden.
Grundsätzlich kann es ähnlich oder eben ganz anders aussehen.
Das Teambild muss ebenfalls geändert werden.

```html
<!DOCTYPE html>
<html lang="de">
<head>
<meta charset="utf-8">
<title>Sehberatung – Mehr Sehen aktiv erleben</title>
<link rel="stylesheet" href="https://fonts.googleapis.com/css2?family=Arimo:wght@400;700&family=PT+Sans+Narrow:wght@400;700&display=swap">
<style>
  :root {
    --green: #4fae4c;
    --green-text: #4ea84d;
    --forest: #2f6b3d;
    --ink: #161616;
    --white: #ffffff;
  }
  * { margin: 0; padding: 0; box-sizing: border-box; }
  html, body { width: 849px; height: 1200px; overflow: hidden; background: var(--white); }
  .flyer {
    position: relative; width: 849px; height: 1200px; overflow: hidden;
    font-family: "Arimo", Arial, sans-serif; color: var(--ink); background: var(--white);
  }
  .team-photo {
    position: absolute; left: 0; top: 0; width: 849px; height: 300px;
    background: linear-gradient(180deg, #d9dadc 0%, #e9e9ea 55%, #ffffff 100%);
  }
  .title-band {
    position: absolute; left: 0; top: 17px; width: 849px; height: 122px;
    background: var(--green); opacity: 0.95;
  }
  .title {
    position: absolute; left: 0; top: 17px; width: 849px; text-align: center;
    font-weight: 700; font-size: 90px; line-height: 1; color: var(--white); letter-spacing: 2px;
  }
  .subtitle {
    position: absolute; left: 0; top: 102px; width: 849px; text-align: center;
    font-weight: 700; font-size: 29px; color: var(--white);
  }
  .partner-card {
    position: absolute; left: 283px; top: 188px; width: 273px; height: 114px;
    background: var(--white); box-shadow: 4px 6px 8px rgba(0,0,0,0.25);
  }
  .partner-mark {
    position: absolute; left: 28px; top: 27px; width: 60px; height: 60px; background: var(--forest);
  }
  .partner-text {
    position: absolute; left: 110px; top: 36px;
    font-family: "PT Sans Narrow", "Arial Narrow", sans-serif; color: #2a2a2a; line-height: 1.15;
  }
  .partner-text .name { font-weight: 700; font-size: 19px; }
  .partner-text .sub { font-size: 19px; }
  .headline {
    position: absolute; left: 0; top: 328px; width: 849px; text-align: center;
    font-weight: 700; font-size: 34.5px; color: var(--forest);
  }
  .intro {
    position: absolute; left: 0; top: 373px; width: 849px; text-align: center;
    font-weight: 700; font-size: 15.3px; line-height: 18.8px;
  }
  .frame-tab { position: absolute; left: 0; top: 430px; width: 270px; height: 30px; background: var(--forest); }
  .frame-side { position: absolute; left: 0; top: 430px; width: 24px; height: 770px; background: var(--forest); }
  .frame-divider { position: absolute; left: 0; width: 270px; background: var(--forest); }
  .frame-foot { position: absolute; left: 0; top: 1170px; width: 849px; height: 30px; background: var(--forest); }
  .photo { position: absolute; }
  .photo-exam { left: 40px; top: 477px; width: 228px; height: 152px;
    background: linear-gradient(135deg, #7d8a99 0%, #c9ccd0 50%, #e8dcd2 100%); }
  .photo-slitlamp { left: 40px; top: 676px; width: 228px; height: 184px;
    background: linear-gradient(135deg, #5f5a58 0%, #c5c8cc 50%, #e9ddd2 100%); }
  .photo-device { left: 38px; top: 906px; width: 232px; height: 247px;
    background: linear-gradient(135deg, #9ea2a8 0%, #d7d9dc 45%, #7d8086 100%); }
  .steps {
    position: absolute; left: 308px; top: 474px; width: 535px;
    font-weight: 700; font-size: 15.6px; line-height: 18.8px;
  }
  .step { margin-bottom: 12.5px; }
  .step-label { color: var(--green-text); }
</style>
</head>
<body>
<div class="flyer">
  <div class="team-photo" role="img" aria-label="Teamfoto: fünf Mitarbeitende in weißen Hemden vor einer Brillenwand"></div>
  <div class="title-band"></div>
  <h1 class="title">SEHBERATUNG</h1>
  <p class="subtitle">Mehr Sehen aktiv erleben</p>

  <div class="partner-card">
    <div class="partner-mark"></div>
    <div class="partner-text">
      <div class="name">Lumaris Vision Experte</div>
      <div class="sub">Seh-Analyse</div>
    </div>
  </div>

  <h2 class="headline">WIR NEHMEN UNS ZEIT FÜR SIE</h2>
  <p class="intro">Bei uns erhalten Sie eine Komfort-Sehberatung, die<br>keine Wünsche offen lässt. Im Einzelnen messen bzw.<br>prüfen wir gemeinsam mit Ihnen</p>

  <div class="frame-tab"></div>
  <div class="frame-side"></div>
  <div class="frame-divider" style="top:651px;height:8px"></div>
  <div class="frame-divider" style="top:876px;height:14px"></div>
  <div class="frame-foot"></div>

  <div class="photo photo-exam" role="img" aria-label="Optikerin misst mit einem Handgerät das Auge einer Kundin"></div>
  <div class="photo photo-slitlamp" role="img" aria-label="Optikerin untersucht eine Kundin an der Spaltlampe"></div>
  <div class="photo photo-device" role="img" aria-label="Vollautomatisches Augendiagnosegerät mit Placido-Ringen"></div>

  <div class="steps">
    <p class="step"><span class="step-label">1. Vorgespräch:</span> Gemeinsam erörtern wir mit Ihnen<br>Ihre Wünsche, Anforderungen und welche Messungen<br>notwendig sind (Anamnese).</p>
    <p class="step"><span class="step-label">2. Vollautomatische Augendiagnose mit Wellenfronttechnologie</span><br>. Objektiver Computersehtest<br>. Wellenfrontmessung<br>. Tag- und Nachtsicht<br>. Transparenzanalyse der Augenlinse (Katarakt Status)<br>. Messung der Hornhauttopografie<br>. Vordere Augenkammeranalyse (Hornhautdicke/<br>Kammerwinkel)</p>
    <p class="step"><span class="step-label">3. Augenglasbestimmung mit</span><br>. Tränenfilmanalyse<br>. Überprüfung des Dämmerungs- und Nachtsehens</p>
    <p class="step"><span class="step-label">4. Weitere Testverfahren</span><br>Weitere Testverfahren führen wir bei Bedarf durch z.B.<br>. Farbtest<br>. Gesichtsfeldmessung / Test für räumliche Wahrnehmung<br>. Winkelfehlsichtigkeiten<br>. Augenhintergrundbetrachtung<br>. Amslertest</p>
    <p class="step"><span class="step-label">5. Sehberatungszertifikat:</span> Die wesentlichen Mess-<br>ergebnisse dokumentieren wir in Ihrem persönlichen<br>Sehberatungszertifikat.</p>
    <p class="step"><span class="step-label">6. Versorgungsvorschlag:</span> Nach der Analyse bespre<br>chen wir mit Ihnen die Wahl der idealen Brillengläser<br>und Fassung.<br>Die beim Augenoptiker durchgeführte Augeninnendruckmessung<br>und andere Screenings geben nur einen Hinweis auf Risikofaktoren<br>und ersetzen keine umfassende ärztliche Untersuchung.</p>
  </div>
</div>
</body>
</html>
```